Biz Card Design TPVC

New business card for a new company.
Logo was completed by a designer on ArtFlock and looking to continue requesting additional services.
Company Name: Tidal Prime Voltage Collective
Although this company is starting in Canada, we will be moving towards a global presence within the next 6 months.
Key elements to this business are as follows.
Energy Procurement
Energy Reduction Services
Demand Side Consulting
Energy Efficiency Consulting
Saving Clients Money
Helping Them Go "Green"
Managing Their Energy Requirements
Basically the goal for our company is to find the best procurement solution for our clients and reduce their energy consumption. This reduces their expenses and the amount of greenhouse gas they produce on a daily basis.
I have been in the energy footprint for the last 20 years and know that most companies are looking to "do whatever is necessary to get them to sign on the dotted line". I would prefer to walk away from a client that I can't help than to put them into a situation that they will regret for years to come. This is where the "TIDAL" part of the company name comes from.
The following is a catch phrase that encompasses what we do.
"Reducing your carbon footprint & energy bill at the same time!"
The back of the card needs to have this statement along with some sort of illustration. The back is a playground for creative ideas.
The front of the card needs the following.
Logo.
First & Last Name (Gus Marwick)
Title (Energy Warrior)
Phone Number (555) 314-2768
Fax Number (555) 862-4091
Email Address gus@tidalprimevoltage.example
Address 47 Orchard Lane Toronto Ontario K4P 2Z7
I want it to be a card that is remembered when any of my staff give it to a customer. It HAS to stand out.
Target Market(s)
Business Owners, Decision Makers, 30 to 65+
Industry/Entity Type
Business
Look and feel
Each slider illustrates characteristics of the customer's brand and the style your logo design should communicate.

```html
<!DOCTYPE html>
<html lang="en">
<head>
<meta charset="utf-8">
<title>Tidal Prime Voltage Collective – Business Card</title>
<link href="https://fonts.googleapis.com/css2?family=PT+Sans:wght@400;700&display=swap" rel="stylesheet">
<style>
  :root {
    --page-bg: #ececec;
    --card-white: #ffffff;
    --green-light: #cfe7a0;
    --green-mid: #6cbf6a;
    --green-deep: #1f8f4a;
    --swoosh: #2fb457;
    --brand-blue: #3a6db3;
    --ink-dark: #333333;
    --ink-mid: #555555;
  }
  * { margin: 0; padding: 0; box-sizing: border-box; }
  html, body {
    width: 1200px; height: 1080px; overflow: hidden;
    background: var(--page-bg);
    font-family: "PT Sans", sans-serif;
  }
  .sheet {
    width: 1200px; height: 1080px;
    display: flex; flex-direction: column; align-items: center; justify-content: center;
    gap: 40px;
  }
  .card {
    position: relative;
    width: 820px; height: 469px;
    overflow: hidden;
    box-shadow: 0 4px 14px rgba(0,0,0,0.18);
  }

  /* Back of card */
  .card-back {
    background: linear-gradient(150deg, var(--green-light) 0%, var(--green-mid) 45%, var(--green-deep) 100%);
  }
  .back-artwork {
    position: absolute; left: 40px; top: 40px;
    width: 420px; height: 400px;
    border-radius: 50%;
    background: radial-gradient(circle at 45% 45%, rgba(255,255,255,0.55), rgba(255,255,255,0.12) 70%, rgba(255,255,255,0) 100%);
  }
  .tagline {
    position: absolute; right: 30px; bottom: 30px;
    text-align: right; color: #fff;
    font-weight: 700; font-size: 28px; line-height: 1.2;
  }

  /* Front of card */
  .card-front { background: var(--card-white); }
  .brand {
    position: absolute; right: 36px; top: 58px;
    display: flex; flex-direction: column; align-items: center; gap: 12px;
  }
  .brand-dot {
    width: 44px; height: 44px; border-radius: 50%;
    background: var(--swoosh);
  }
  .brand-name {
    color: var(--brand-blue);
    font-weight: 700; font-size: 31px; letter-spacing: -0.5px;
  }
  .person {
    position: absolute; right: 36px; top: 238px; text-align: right;
  }
  .person-name { color: var(--ink-dark); font-weight: 700; font-size: 38px; line-height: 1; }
  .person-title { color: var(--ink-mid); font-size: 20px; margin-top: 6px; }
  .swoosh { position: absolute; left: 0; top: 0; }
  .contact {
    position: absolute; bottom: 26px;
    font-size: 19px; line-height: 1.45; color: var(--ink-mid);
  }
  .contact-phones { left: 30px; text-align: right; }
  .contact-web { right: 36px; text-align: right; }
  .label { color: var(--brand-blue); font-weight: 700; }
</style>
</head>
<body>
<main class="sheet">
  <section class="card card-back">
    <div class="back-artwork" role="img" aria-label="Large leaf with lightning bolt illustration"></div>
    <p class="tagline">Reducing your carbon<br>footprint &amp; energy bill at the same time!</p>
  </section>

  <section class="card card-front">
    <svg class="swoosh" width="820" height="469" viewBox="0 0 820 469" aria-hidden="true">
      <path d="M180 372 C 380 330, 640 322, 820 345 L 820 395 C 640 362, 420 350, 180 372 Z" fill="var(--swoosh)"/>
    </svg>
    <div class="brand">
      <span class="brand-dot"></span>
      <span class="brand-name">Tidal Prime Voltage Collective</span>
    </div>
    <div class="person">
      <p class="person-name">Gus Marwick</p>
      <p class="person-title">Energy Warrior</p>
    </div>
    <div class="contact contact-phones">
      <p><span class="label">Phone:</span> (555) 314-2768</p>
      <p><span class="label">Fax:</span> (555) 862-4091</p>
    </div>
    <div class="contact contact-web">
      <p><span class="label">Email:</span> gus@tidalprimevoltage.example</p>
      <p><span class="label">Address:</span> 47 Orchard Lane Toronto Ontario K4P 2Z7</p>
    </div>
  </section>
</main>
</body>
</html>
```